Australian Meat, Seafood and Fresh Produce Website

Our organization is looking to design a simple, but eye catching website to show our services.
Our company exports West Australian FRESH fruit and vegetables, seafood and meat.
The website we are looking for would consist of:
- Landing Page
- Company info
- Directors bio
- Page that highlights our products
- Contact us page
We would like it to have a Chinese translated version as well.
Tobin
Target Market(s)
Chinese Market
Industry/Entity Type
It Company
Number of Pages Required
1 page
Look and feel
Each slider illustrates characteristics of the customer's brand and the style your logo design should communicate.

```html
<!DOCTYPE html>
<html lang="en">
<head>
<meta charset="utf-8">
<title>Fresh Export – Meat, Seafood and Fresh Produce</title>
<link href="https://fonts.googleapis.com/css2?family=Open+Sans:wght@400;600;700;800&display=swap" rel="stylesheet">
<style>
:root{
  --ink:#333;
  --muted:#888;
  --line:#e3e3e3;
  --orange:#f7931e;
  --amber:#f9b233;
  --green:#8cc63f;
  --teal:#2ec4a6;
  --red:#e8413c;
  --dark:#2f2f2f;
  --paper:#fff;
  --soft:#f6f6f6;
}
*{box-sizing:border-box;margin:0;padding:0}
html,body{width:1200px;height:2840px;overflow:hidden;background:var(--paper);font-family:"Open Sans",Arial,sans-serif;color:var(--ink)}
.page{position:relative;width:1200px;height:2840px}
.abs{position:absolute}
.wrap{position:absolute;left:240px;width:720px}

/* hero */
.hero{position:absolute;left:0;top:0;width:1200px;height:420px;background:linear-gradient(100deg,#5c8a3a 0%,#7aa84b 30%,#b9a27a 55%,#c0504a 75%,#8e2f2c 100%)}
.logo{position:absolute;left:240px;top:0;width:160px;height:60px;background:var(--dark);color:#fff;font-weight:700;font-size:22px;letter-spacing:2px;display:flex;align-items:center;justify-content:center}
.nav{position:absolute;left:240px;top:72px;width:720px;height:24px;background:#fff;display:flex;gap:0}
.nav a{flex:1;text-align:center;font-size:9px;line-height:24px;color:var(--ink);text-decoration:none;font-weight:600;border-right:1px solid var(--line)}
.nav a.on{background:var(--orange);color:#fff}
.hero h1{position:absolute;left:270px;top:150px;color:#fff;font-size:32px;font-weight:800}
.hero p{position:absolute;left:270px;top:205px;width:280px;color:#fff;font-size:14px;line-height:19px;font-weight:600}
.btn{display:inline-block;background:var(--orange);color:#fff;font-size:11px;font-weight:700;padding:7px 14px;border-radius:2px}
.hero .btn{position:absolute;left:270px;top:322px}

/* features */
.features{top:432px;height:220px;display:flex}
.feature{flex:1;padding:22px 16px;color:#fff;position:relative}
.feature h3{font-size:21px;font-weight:800;line-height:24px}
.feature small{display:block;font-size:12px;margin-top:2px}
.feature .more{position:absolute;left:16px;bottom:22px;font-size:10px;font-weight:700}

/* headings */
.sec-title{position:absolute;left:0;width:1200px;text-align:center;font-size:17px;font-weight:800;letter-spacing:1px}
.sec-sub{position:absolute;left:0;width:1200px;text-align:center;font-size:10px;color:var(--muted);letter-spacing:1px}
.sec-rule{position:absolute;left:240px;width:720px;height:1px;background:var(--line)}
.sec-rule span{position:absolute;left:50%;top:-12px;transform:translateX(-50%);background:#fff;padding:0 16px;font-size:16px;font-weight:800;letter-spacing:1px;white-space:nowrap}

/* products */
.products{top:790px;display:flex}
.product{flex:1;text-align:center}
.product .ph{width:130px;height:110px;margin:0 auto;border-radius:8px}
.product h4{font-size:12px;font-weight:600;margin-top:60px}
.stars{color:var(--orange);font-size:13px;letter-spacing:1px}
.price{color:var(--orange);font-size:13px;font-weight:700}

/* news */
.news{top:1180px;display:flex;gap:10px}
.news-card{flex:1;height:140px;position:relative;border-radius:2px}
.news-card .date{position:absolute;left:0;top:0;width:40px;height:46px;color:#fff;text-align:center;font-weight:800;font-size:18px;line-height:24px;padding-top:4px}
.news-card .date small{display:block;font-size:9px;line-height:12px;font-weight:600}

/* achievements */
.panel{position:absolute;border:1px solid var(--line);background:#fff}
.profile{left:240px;top:1425px;width:165px;height:300px;text-align:center;padding-top:22px}
.avatar{width:90px;height:90px;border-radius:50%;margin:0 auto;background:linear-gradient(#d9c4b0,#a98a70)}
.profile h5{font-size:11px;font-weight:700;margin-top:22px}
.profile em{display:block;font-style:normal;font-size:10px;color:var(--orange)}
.btn-grey{display:inline-block;background:#9a9a9a;color:#fff;font-size:10px;padding:5px 12px;margin-top:12px}
.event{left:420px;top:1410px;width:360px;height:315px;padding:0}
.tabs{display:flex;justify-content:center;gap:0;margin-top:0}
.tabs span{font-size:10px;padding:7px 14px;border:1px solid var(--line);border-top:none;background:var(--soft);color:var(--muted)}
.tabs span.on{background:#fff;color:var(--ink);font-weight:700}
.event-body{padding:18px 26px}
.event h4{font-size:18px;line-height:22px;font-weight:600}
.countdown{display:flex;gap:14px;font-size:30px;font-weight:800;margin-top:12px;letter-spacing:1px}
.cd-labels{display:flex;gap:36px;font-size:9px;color:var(--muted);margin-top:2px}
.event h6{font-size:12px;font-weight:700;margin-top:18px}
.event p{font-size:10px;color:var(--muted);line-height:14px;margin-top:4px}
.event .link{font-size:10px;font-weight:700;margin-top:14px;display:block}
.pricecard{left:798px;top:1425px;width:162px;height:300px;text-align:center;padding-top:20px}
.pricecard h5{font-size:15px;font-weight:400;color:#666;line-height:19px}
.pricecard .big{font-size:34px;color:var(--orange);font-weight:800;margin:20px 0 18px}
.pricecard .big sup{font-size:16px}
.pricecard ul{list-style:none;text-align:left;padding-left:30px;font-size:10px;color:var(--muted);line-height:17px}
.pricecard ul li::before{content:"› ";color:var(--orange)}
.pricecard .btn{margin-top:16px}

/* buy */
.slider-arrows{position:absolute;left:916px;top:1806px;display:flex;gap:4px}
.slider-arrows span{width:18px;height:18px;border:1px solid var(--line);font-size:11px;line-height:16px;text-align:center;color:var(--muted)}
.buy{top:1835px;display:flex;gap:15px}
.buy-card{flex:1;height:165px;position:relative;padding:10px 12px;color:#fff}
.buy-card h4{font-size:13px;font-weight:700}
.buy-card .amt{font-size:36px;font-weight:800;line-height:40px}
.buy-card .amt sup{font-size:15px}
.buy-card .old{font-size:13px;text-decoration:line-through;opacity:.8;margin-right:4px;font-weight:600}
.buy-card .ph{position:absolute;right:10px;bottom:8px;width:120px;height:80px;border-radius:40px}

/* partners */
.partners{top:2140px;display:flex;justify-content:space-between;align-items:center;padding:0 10px}
.badge{width:130px;height:26px;border-radius:13px;background:#cfcfcf}

/* banner */
.banner{position:absolute;left:0;top:2240px;width:1200px;height:240px;background:linear-gradient(90deg,#b8382c 0%,#d9822b 30%,#9aa83a 60%,#5d8d2e 100%)}
.banner h2{position:absolute;left:0;width:1200px;top:70px;text-align:center;color:#fff;font-size:34px;font-weight:800}
.banner .btn{position:absolute;left:560px;top:140px;padding:8px 20px}

/* tweet */
.tweet{top:2508px;display:flex;align-items:flex-start;gap:14px}
.tweet .dot{width:22px;height:22px;border-radius:50%;background:#3aa3e3;flex:none}
.tweet p{font-size:10px;color:var(--muted);line-height:14px;width:420px}
.tweet time{margin-left:auto;font-size:10px;color:var(--muted)}

/* footer */
.footer{top:2570px;display:flex;border-top:1px solid var(--line);padding-top:16px}
.fcol{flex:1}
.fcol h6{font-size:11px;font-weight:700;letter-spacing:1px;margin-bottom:10px}
.fcol ul{list-style:none;font-size:10px;color:var(--muted);line-height:24px}
.bottom{top:2800px;display:flex;font-size:9px;color:var(--muted);border-top:1px solid var(--line);padding-top:10px}
</style>
</head>
<body>
<div class="page">

  <header class="hero" role="img" aria-label="Photo of fresh raw meat with green herbs on a wooden board">
    <div class="logo">LOGO</div>
    <nav class="nav">
      <a class="on">HOME</a><a>ABOUT US</a><a>SHOP</a><a>PRODUCTS</a><a>DELIVERY</a><a style="border-right:none">CONTACT</a>
    </nav>
    <h1>We Export Best Meat</h1>
    <p>Voluptas assumenda est omnis dolor repellendus Temporibus autem qui buxdam et aut officiis</p>
    <span class="btn">Read More</span>
  </header>

  <section class="wrap features">
    <div class="feature" style="background:var(--orange)"><h3>Best Price</h3><small>Always</small><span class="more">Read More »</span></div>
    <div class="feature" style="background:var(--amber)"><h3>Premium</h3><small>Quality</small><span class="more">Read More »</span></div>
    <div class="feature" style="background:var(--green)"><h3>Organic</h3><small>100% Healthy</small><span class="more">Read More »</span></div>
    <div class="feature" style="background:var(--teal)"><h3>Shipping</h3><small>Free</small><span class="more">Read More »</span></div>
  </section>

  <h2 class="sec-title" style="top:708px">BEST QUALITY FRESH PRODUCTS</h2>
  <p class="sec-sub" style="top:736px">NAM LIBERO TEMPORE, CUM SOLUTA NOBIS EST ELIGENDI OPTIO</p>

  <section class="wrap products">
    <div class="product"><div class="ph" role="img" aria-label="Fresh peppers and vegetables" style="background:linear-gradient(135deg,#e63b2e,#f3c338 55%,#5a9a35)"></div><h4>Fresh Vegetables</h4><div class="stars">★★★★★</div><div class="price">$ 13.21</div></div>
    <div class="product"><div class="ph" role="img" aria-label="Fresh mango fruit" style="background:linear-gradient(135deg,#f7c43a,#ef8a1f 60%,#5c9a35)"></div><h4>Fresh Fruits</h4><div class="stars">★★★★★</div><div class="price">$ 13.58</div></div>
    <div class="product"><div class="ph" role="img" aria-label="Fresh oysters" style="background:linear-gradient(135deg,#8b8a72,#5f6048)"></div><h4>Sea Food</h4><div class="stars">★★★★★</div><div class="price">$ 34.41</div></div>
    <div class="product"><div class="ph" role="img" aria-label="Raw red meat cut" style="background:linear-gradient(135deg,#c2303a,#7f1d24)"></div><h4>Meat</h4><div class="stars">★★★★★</div><div class="price">$ 19.61</div></div>
  </section>

  <div class="sec-rule" style="top:1110px"><span>LATEST NEWS</span></div>
  <section class="wrap news">
    <div class="news-card" role="img" aria-label="Fresh salmon steaks" style="background:linear-gradient(135deg,#e8763a,#b7492a)"><div class="date" style="background:var(--orange)">20<small>MAY</small></div></div>
    <div class="news-card" role="img" aria-label="Ripe fruits on a market stall" style="background:linear-gradient(135deg,#d24c2c,#e9a13b)"></div>
    <div class="news-card" role="img" aria-label="Bunches of grapes on the vine" style="background:linear-gradient(135deg,#4c7b2e,#2c4b25)"><div class="date" style="background:var(--green)">14<small>MAY</small></div></div>
    <div class="news-card" role="img" aria-label="Basket of red tomatoes" style="background:linear-gradient(135deg,#c93c2a,#8e2a1f)"><div class="date" style="background:var(--teal)">07<small>MAY</small></div></div>
  </section>

  <div class="sec-rule" style="top:1372px"><span>OUR ACHIEVEMENTS</span></div>
  <div class="panel profile">
    <div class="avatar" role="img" aria-label="Portrait photo of the director"></div>
    <h5>Jared Tobin</h5><em>Director</em>
    <span class="btn-grey">Read More</span>
  </div>
  <div class="panel event">
    <div class="tabs"><span class="on">Next Event</span><span>Selection</span><span>Export</span></div>
    <div class="event-body">
      <h4>Et harum quidem rerum facilis expedita</h4>
      <div class="countdown"><span>125</span>:<span>02</span>:<span>17</span>:<span>49</span></div>
      <div class="cd-labels"><span>Days</span><span>Hours</span><span>Minutes</span><span>Seconds</span></div>
      <h6>Et harum quidem rerum facilis expedita</h6>
      <p>Nam libero tempore cum soluta nobis est eligendi</p>
      <span class="link">View More</span>
    </div>
  </div>
  <div class="panel pricecard">
    <h5>Fresh<br>Vegetables</h5>
    <div class="big"><sup>$</sup>24.85</div>
    <ul><li>Fresh Picked</li><li>Local Farms</li><li>Fast Export</li></ul>
    <span class="btn">Read More</span>
  </div>

  <div class="sec-rule" style="top:1792px"><span>BUY OUR BEST PRODUCTS</span></div>
  <div class="slider-arrows"><span>‹</span><span>›</span></div>
  <section class="wrap buy">
    <div class="buy-card" style="background:var(--orange)"><h4>Fresh Carrots</h4><div class="amt"><span class="old">$20</span><sup>$</sup>15</div><div class="ph" role="img" aria-label="Bunch of carrots" style="background:linear-gradient(90deg,#f0601f,#d84a12)"></div></div>
    <div class="buy-card" style="background:var(--green)"><h4>Fresh Berries</h4><div class="amt"><span class="old">$18</span><sup>$</sup>12</div><div class="ph" role="img" aria-label="Pile of blueberries" style="background:linear-gradient(90deg,#3b4a8a,#202a5e)"></div></div>
    <div class="buy-card" style="background:var(--teal)"><h4>Fresh Meat</h4><div class="amt"><span class="old">$21</span><sup>$</sup>16</div><div class="ph" role="img" aria-label="Raw steak cuts" style="background:linear-gradient(90deg,#c73b3f,#8e2127)"></div></div>
  </section>

  <div class="sec-rule" style="top:2082px"><span>PARTNERS</span></div>
  <section class="wrap partners">
    <div class="badge"></div><div class="badge"></div><div class="badge"></div><div class="badge"></div>
  </section>

  <section class="banner" role="img" aria-label="Photo of a market table full of fresh fruit and vegetables">
    <h2>As Delicious As Ever</h2>
    <span class="btn">BUY NOW</span>
  </section>

  <section class="wrap tweet">
    <span class="dot"></span>
    <p>Sed ut perspiciatis unde omnis iste natus error sit voluptatem accusantium doloremque laudantium totam rem</p>
    <time>1 week ago</time>
  </section>

  <footer class="wrap footer">
    <div class="fcol"><h6>SERVICES</h6><ul><li>Delivery</li><li>Wholesale</li><li>Export</li><li>Storage</li><li>Packing</li></ul></div>
    <div class="fcol"><h6>LINKS</h6><ul><li>About Us</li><li>Shop</li><li>Products</li><li>Delivery</li><li>Contact</li></ul></div>
    <div class="fcol"><h6>PRODUCTS</h6><ul><li>Vegetables</li><li>Fruits</li><li>Seafood</li><li>Meat</li><li>Dairy</li></ul></div>
    <div class="fcol"><h6>BLOG</h6><ul><li>Recipes</li><li>Farming</li><li>Export News</li><li>Seasons</li><li>Events</li></ul></div>
  </footer>
  <div class="wrap bottom"><span>© Copyright Fresh Export 2024</span></div>

</div>
</body>
</html>
```